We are launching a National Program and plan to use this brochure to describe the program. This objective of this brochure is to introduce the program and its benefits and hopefully entice companies to join our network or even inspire individuals who are currently working in the field of commissioning to start a new company and joining our network as a key strategy in launching there new company.

What we are looking for is a brochure at 8x11 four page where we will print on 12x18 (front-to-back) and then trim to 11x17 and fold in half. We want it to look very professional and encourage bleeding graphics to the edge.

vantorix has been in business for 15 years and we have standard branding that we use which includes a logo, project sheets, resumes, news letters etc. All out graphics and templates are done using Adobe Illustrator and InDesign. We use photoshop to dress up pictures. We would like to use our branding concepts with this brochure but at the same time are open to new ideas.

We do not want to limit the creativity of the designer

Anyone interested in working on this project can send me a email requesting files that support this project and we will send a link to a FTP site for you can obtain the files and save you time for working on this brochure

Please email me at milo@vantorix.example and you will be added to the distribution and the shared folder from our FTP site

You can also visit our web site at www.vantorix.example to lean more about our company

vantorix National Commissioning Program

Brochure Outline

 

Page 1 FRONT COVER

 

National Commissioning Network Program

 

Since 1995, vantorixhas offered commissioning services.We’re progressive, experienced firm that has developed a unique approachto commissioning using a software tool kit that simplifies the commissioningprocess allowing you to spend time on what is important and that is doing theactual work of commissioning.

 

We are in the process of signing up commissioning agents whoare interested in playing in the commissioning field on a National Level. 

 

HOW IT WORKS

 

Being part of the vantorixNational Commissioning Network gives you access to the other commissioningagents on a National Level allowing you to combine your forces with other CommissioningAgents (CxA’s) and tackle the larger projects without staffing up.

 

Benefits include:

 

·Access and use of vantorix’s software commissioning tool kit that simplifies thecommissioning process by providing standardization among all your field technicianson every project.  The tool kit providesa database of real time record of data acquisition and project issues for youknow where you are at on every project daily.

·Combining forces with other commissioning agentsin the program on a National basis gives you access to staff-up for a projectwithout the cost.  In addition, giventhat everyone in the program utilizes the same tool kit for data acquisitionand commissioning documentation and reporting you can be assured whoever isworking on your project is doing the job the right and consistent with yourstaff.

·Using National Network we as a group can goafter National Accounts and provide the client with a consistent product acrossthe board regardless of location.Currently there is no one who can provide this type of service withconsistency at this level

·Using the national database of projects you cansubmit on potential projects with confidence knowing your qualifications combinewith the national network of commissioning agents can back you up on any sizeproject.

·vantorixwill provide Marketing support if you are part of the National Network.  Marketing support will include project andemployee resumes using your logo on customized marketing material.  This will allow the new start-up company’s tocompete on day 1 and allow the smaller company to compete for larger projects.

·Training will be provided for all NationalNetwork members.  Training will beprovided on the use of the commissioning kit as well as specialized classesdesign specifically to teach the art of commissioning

·Using the vantorix tool kit makes Allied Federal Eco Structures Board (AFESB) www.afesb.example/ BRIX Certification for EnhancedCommissioning a breeze by automatic generation of test scripts, functionaltesting, commissioning reports and energy use evaluation.  Other accessories with the tool kit includesetting up and providing a Monitoring and Verification program which providesadditional 2 points for the BRIX Certification Program.

·Provide values added services such as Monitoringand Verification on your BRIX projects and have the reports automaticallyformatted and emailed to you in real time.

 

Front cover Graphics will be the key for catching attention.  Will provide numerous pictures and logos forwe can get a cool design. 

 

Page 2 and 3  INSIDE BROCHURE

 

The inside pages will be dedicated to the Commissioning ToolKit.  Text and generic layout informationwill be provided by Dennis

 

Need to use the attached document Qz Pack Notes2.doc toprovide text that will highlight the tool kit capabilities

 

Page 4  BACKCOVER

 

QUALIFY TO BECOME AMEMBER

Need to tell how you can qualifyto become a member of the vantorixNational Commissioning Network

·vantorixwebsite will need to have a link a pages dedicated to signing up for membershipdedicated to allowing a potential.  Also,

·Members will have territorial rights.  Meaning by signing up earlier you can beassured that your business has first right for projects in your city forNational Accounts

·Can provide assistance for Business Start-up byproviding project and employee resumes.In addition, can provide mentoring to small business start-up aloowingyou to take charge of your career

 

MEMBER DIRECTORY

Copperline Commissioning located inHouston, Texas is the first member organization to join the vantorix NationalNetwork.  Copperline Commissioning is aHistorically Underutilized Business in the State of Texas and is providingopportunities for employment in Texas

Like Copperline your firm can be aNational Player in the excited field of Commissioning and have the software,mentoring, training and knowledge that you can do the job and exceed yourclient expectations.

Graphics on the back page need to include a National Map with majorcities shown highlighting where vantorix has provided services as well as Copperline logo in Houston showing them as a National Partner

 

Need to include vantorix logo and contact information

 

 

What is it

 

1.     Weare going to create a national program where we sign-up Commissioning Agentsand companies to be part of the network.

2.     Bybeing a network partner we will provide training on using our commissioningsoftware tool kit.  This tool kit isunique and provides automatic commissioning plan development, commissioningreports and data collection in a database structure that will allow thecommissioning agent (CxA) to provide consistent services regardless of clientand who is working on the project.  (Seebrochure layout for additional information)

3.     Wewill provide mentoring for smaller companies who are just getting started inthe business

4.     Bybeing a member a commissioning company will use of our software tool kit.  The idea is to have a national organizationusing the same means and methods for providing commissioning services forbuildings.  By doing this we can gainnational recognition and obtain national accounts for larger corporations whoown real-estate.

5.     Beingpart of a national network will allow you to use resources from othercommissioning providers.  Since thecommissioning business staffing can be hard to manage this will allow a companyto go after larger projects without staffing up for just the one project.

 

 

HOW WILL IT WORK

 

When a commissioning agent (CxA) or company signs up thatwill sign a contact with vantorix that will allow them to use the software tookkit as long as they are in good membership standing.

 

To promote membership initially we are going to get CxA’s tosign up and pay us by marking up there first $200,000 in fees using the programby 10%.  We will give them 1 full year tobook the business and make the payment of $20,000.  After the first year and initial membershipthe annual fees will be $6,000.  Thiswill pay for membership organizational cost and to support CxA’s in going afternational projects

 

We will maintain the national database of projects andpersonnel and orchestrate resources for members.  We will provide a mark-up on staff by 10% andbe used as a broker for all the CxA’s to staff their projects.

 

We will provide support and training to the CxA’s to helpthem get projects using project and personnel resumes from all the nationalmembers

 

We will mentor smaller companies on how to establish a smallbusiness.  This will include how to get aweb site, email, phone systems and contracts

 

 

MEMBERS

 

The first member company is Copperline Commissioning, LLClocated in Houston Texas.  This companyis a minority company and is registered as a Historically Under UtilizedBusiness (HUB) in the state of Texas.Copperline will be the example company for all future national members

 

 

 

vantorix BENEFITS

 

1.National platform for we can go after nationalaccounts.

 

2.Allow us to get involved in projects on anational basis to help promote our design engineering business by providingdesign services.  Given that mostcommission projects expose mechanical and electrical failures that need to beupgraded in buildings we can support the CxA’s by providing engineeringsupport.  This will allow us to expandour engineering company.

 

3.Assist us in expanding vantorix without the cost of marketing and opening up branch offices.

4.Companies that become members that prove to besuperior we can look at acquiring to expand the vantorix network.

 

5.Provide a national program for launching thetool kit software that we developed.  

    Increase our project resume and personnelresumes

 

7.Increase sales and profits

```html
<!DOCTYPE html>
<html lang="en">
<head>
<meta charset="utf-8">
<title>vantorix – National Commissioning Network Program</title>
<link rel="stylesheet" href="https://fonts.googleapis.com/css2?family=Nunito:wght@800;900&family=Open+Sans:wght@400;700&display=swap">
<style>
  :root {
    --green: #a3cf55;
    --green-ring: #8cc63f;
    --green-label: #9ccf4a;
    --navy: #1a3566;
    --navy-title: #17346a;
    --white: #ffffff;
    --paper: #f4f5f6;
  }
  html, body {
    margin: 0;
    padding: 0;
    overflow: hidden;
  }
  .brochure-cover {
    position: relative;
    width: 927px;
    height: 1200px;
    overflow: hidden;
    background: var(--paper);
    font-family: "Open Sans", Arial, sans-serif;
  }
  .cover-shapes {
    position: absolute;
    inset: 0;
  }
  .brand-name {
    position: absolute;
    left: 28px;
    top: 96px;
    margin: 0;
    font-family: "Open Sans", Arial, sans-serif;
    font-weight: 700;
    font-size: 40px;
    letter-spacing: 0.5px;
    color: var(--white);
    line-height: 1;
  }
  .brand-dot {
    position: absolute;
    left: 140px;
    top: 22px;
    width: 62px;
    height: 62px;
    border: 4px solid var(--white);
    border-radius: 50%;
    box-sizing: border-box;
  }
  .cover-title {
    position: absolute;
    right: 30px;
    top: 24px;
    margin: 0;
    font-family: "Nunito", "Arial Rounded MT Bold", sans-serif;
    font-weight: 900;
    color: var(--navy-title);
    text-align: center;
    line-height: 1;
    text-shadow: 0 0 2px rgba(255,255,255,0.9);
  }
  .cover-title .title-line-one {
    display: block;
    font-size: 41px;
    letter-spacing: 0.5px;
  }
  .cover-title .title-line-two {
    display: block;
    font-size: 53px;
    letter-spacing: 1px;
    margin-top: 2px;
  }
  .intro-text {
    position: absolute;
    left: 26px;
    top: 902px;
    width: 875px;
    margin: 0;
    font-size: 13.4px;
    line-height: 1.45;
    color: var(--white);
    text-align: justify;
  }
  .program-heading {
    position: absolute;
    left: 0;
    width: 860px;
    top: 986px;
    margin: 0;
    text-align: center;
    font-size: 17px;
    font-weight: 700;
    font-variant: small-caps;
    letter-spacing: 2px;
    color: var(--green-label);
  }
  .program-benefits {
    position: absolute;
    left: 26px;
    top: 1013px;
    width: 880px;
    margin: 0;
    padding: 0;
    list-style: none;
    display: grid;
    grid-template-columns: 298px 297px 285px;
    row-gap: 26px;
  }
  .program-benefits li {
    font-size: 19px;
    font-weight: 700;
    line-height: 1.38;
    color: var(--white);
    padding-right: 12px;
  }
</style>
</head>
<body>
<main class="brochure-cover">
  <svg class="cover-shapes" width="927" height="1200" viewBox="0 0 927 1200" aria-hidden="false">
    <defs>
      <linearGradient id="tone-machinery" x1="0" y1="0" x2="1" y2="1">
        <stop offset="0" stop-color="#6d8aa3"/>
        <stop offset="0.55" stop-color="#b73a2c"/>
        <stop offset="1" stop-color="#4a4f55"/>
      </linearGradient>
      <linearGradient id="tone-facade" x1="0" y1="0" x2="1" y2="1">
        <stop offset="0" stop-color="#2f6fc7"/>
        <stop offset="0.6" stop-color="#8fb2d6"/>
        <stop offset="1" stop-color="#c8bfae"/>
      </linearGradient>
      <linearGradient id="tone-atrium" x1="0" y1="0" x2="0" y2="1">
        <stop offset="0" stop-color="#3b4f78"/>
        <stop offset="0.6" stop-color="#d8a648"/>
        <stop offset="1" stop-color="#3a3a3e"/>
      </linearGradient>
      <linearGradient id="tone-workstation" x1="0" y1="0" x2="1" y2="1">
        <stop offset="0" stop-color="#cfd6dc"/>
        <stop offset="0.6" stop-color="#7e9a7a"/>
        <stop offset="1" stop-color="#2c2f33"/>
      </linearGradient>
      <linearGradient id="tone-panel" x1="0" y1="0" x2="1" y2="1">
        <stop offset="0" stop-color="#8e9497"/>
        <stop offset="1" stop-color="#3c4145"/>
      </linearGradient>
      <linearGradient id="tone-backdrop" x1="0" y1="0" x2="1" y2="0">
        <stop offset="0" stop-color="#f7f7f7"/>
        <stop offset="1" stop-color="#e6e7e8"/>
      </linearGradient>
    </defs>

    <!-- light backdrop -->
    <rect class="backdrop" x="0" y="0" width="927" height="1200" fill="url(#tone-backdrop)"/>

    <!-- green header band with curved lower edge -->
    <path class="header-band" d="M0,0 H927 V128 C700,128 420,140 250,190 C140,222 60,300 0,380 Z" fill="var(--green)"/>

    <!-- green connectors between circles -->
    <path class="circle-link" d="M742,330 C760,520 820,600 803,765" fill="none" stroke="var(--green-ring)" stroke-width="70" stroke-linecap="round"/>
    <path class="circle-link" d="M455,758 C560,700 680,720 803,765" fill="none" stroke="var(--green-ring)" stroke-width="46" stroke-linecap="round"/>
    <path class="circle-link" d="M182,424 C300,560 380,640 455,758" fill="none" stroke="var(--green-ring)" stroke-width="40" stroke-linecap="round"/>

    <!-- navy base with curved top -->
    <path class="navy-base" d="M0,560 C110,630 200,760 330,840 C420,885 520,880 927,830 V1200 H0 Z" fill="var(--navy)"/>

    <!-- photo circles -->
    <circle cx="182" cy="424" r="170" fill="url(#tone-machinery)" stroke="var(--green-ring)" stroke-width="20" role="img" aria-label="Photo of a red pump motor with piping in a mechanical room"/>
    <circle cx="742" cy="326" r="176" fill="url(#tone-facade)" stroke="var(--green-ring)" stroke-width="20" role="img" aria-label="Photo of a modern glass-fronted building entrance under blue sky"/>
    <circle cx="455" cy="758" r="146" fill="url(#tone-atrium)" stroke="var(--green-ring)" stroke-width="20" role="img" aria-label="Photo of a lit glass stairwell tower at dusk"/>
    <circle cx="803" cy="765" r="130" fill="url(#tone-workstation)" stroke="var(--green-ring)" stroke-width="20" role="img" aria-label="Photo of a technician at a computer workstation"/>
    <circle cx="50" cy="803" r="92" fill="url(#tone-panel)" stroke="var(--green-ring)" stroke-width="18" role="img" aria-label="Photo of electrical switchgear panel"/>
  </svg>

  <span class="brand-dot" aria-hidden="true"></span>
  <p class="brand-name">vantorix</p>

  <h1 class="cover-title">
    <span class="title-line-one">National Commissioning</span>
    <span class="title-line-two">Network Program</span>
  </h1>

  <p class="intro-text">vantorix has offered has offered commissioning services since 1995. We’re a progressive, experienced firm that has developed a unique approach to commissioning using a software tool kit that simplifies the commissioning process. Our kit enables you to spend more time on what is important... doing the actual work of commissioning.</p>

  <h2 class="program-heading">Our Program</h2>

  <ul class="program-benefits">
    <li>Access to our proprietary commissioning tool kit</li>
    <li>Keeps you up to date on your project in real-time</li>
    <li>Makes BRIX Certification a breeze</li>
    <li>Helps to simplify the commissioning process</li>
    <li>Enables you to combine forc-es with other commissioning agents at low cost</li>
    <li>Provides monitoring and verification on your BRIX projects</li>
  </ul>
</main>
</body>
</html>
```